Letterhead Design Needed for Real Estate Office

We are a boutique real estate agency focused on property management. We need a letter head which is professional looking and include the following information:

Logo
ABN Number
Address
Postal Address
Phone
Fax
Mobile
Email
Website

Please note that the PLVAQT logo can not be changed and must be positioned at the bottom right corner.

Please find attached the existing letterhead design for all the required elements.

Target Market(s)

Letterhead mostly used for service of notices, business letters, clients communication

Industry/Entity Type

Boutique

Colors

Designer to choose colors to be used in the design.

Requirements
Must have
• Logo

```html
<!DOCTYPE html>
<html lang="en">
<head>
<meta charset="utf-8">
<title>Meridian Partners Real Estate – Letterhead</title>
<link href="https://fonts.googleapis.com/css2?family=Open+Sans:wght@400;600;700&display=swap" rel="stylesheet">
<style>
  :root {
    --backdrop: #e8e8e9;
    --paper: #ffffff;
    --green-band: #5fa33a;
    --green-light: #9bbd3c;
    --green-mid: #6a9f3f;
    --green-deep: #4f8a3a;
    --ink: #2b2b2b;
    --ink-soft: #555;
    --partner-blue: #1f6fb4;
  }
  * { box-sizing: border-box; margin: 0; padding: 0; }
  html, body { width: 1200px; height: 795px; overflow: hidden; }
  body {
    background: var(--backdrop);
    font-family: "Open Sans", Arial, sans-serif;
    color: var(--ink);
    position: relative;
  }
  .letterhead {
    position: absolute;
    left: 330px; top: 16px;
    width: 540px; height: 763px;
    background: var(--paper);
    box-shadow: 0 2px 8px rgba(0,0,0,.12);
    overflow: hidden;
  }
  .top-band {
    position: absolute; left: 0; top: 0; width: 100%; height: 7px;
    background: var(--green-band);
  }
  .brand {
    position: absolute; left: 44px; top: 66px;
    display: flex; align-items: center; gap: 8px;
  }
  .brand-square { width: 18px; height: 18px; background: var(--green-mid); }
  .brand-name {
    font-weight: 700; font-size: 15px; letter-spacing: .5px;
    color: var(--ink); line-height: 1.1;
  }
  .contact {
    position: absolute; right: 44px; top: 46px;
    font-size: 6.2px; line-height: 1.55; color: var(--ink-soft);
    display: grid; grid-template-columns: auto auto auto; column-gap: 22px;
  }
  .contact .wide { grid-column: 1 / -1; }
  .letter-body {
    position: absolute; left: 118px; top: 160px; width: 360px;
    font-size: 8.4px; line-height: 1.5; color: var(--ink);
  }
  .letter-body p { margin-bottom: 11px; }
  .corner-art {
    position: absolute; left: 0; bottom: 0; width: 330px; height: 190px;
    background: linear-gradient(135deg, var(--green-light) 0%, var(--green-mid) 55%, var(--green-deep) 100%);
  }
  .partner {
    position: absolute; right: 44px; bottom: 188px;
    display: flex; align-items: center; gap: 7px;
  }
  .partner-shape { width: 14px; height: 14px; background: var(--partner-blue); }
  .partner-label { display: flex; flex-direction: column; align-items: flex-end; }
  .partner-member { font-size: 8px; color: var(--ink-soft); line-height: 1; }
  .partner-name { font-size: 17px; font-weight: 600; color: var(--partner-blue); line-height: 1.1; }
</style>
</head>
<body>
  <main class="letterhead">
    <div class="top-band"></div>

    <header class="brand">
      <span class="brand-square"></span>
      <span class="brand-name">MERIDIAN PARTNERS</span>
    </header>

    <address class="contact">
      <span>ABN 12 345 678 901</span><span>F 9400 1234</span><span>E info@meridianpr.example</span>
      <span>M 0400 123 456</span><span>P 9400 5678</span><span>W www.meridianpr.example</span>
      <span class="wide">Shop 12, 88 Harbour Road Lindfield NSW 2070 Australia</span>
      <span class="wide">PO Box 450 Lindfield NSW 2070</span>
    </address>

    <section class="letter-body">
      <p>Lorem ipsum dolor sit amet, consectetur adipiscing elit. In rutrum et odio vitae porta. Ut in lectus vitae lorem porttitor iaculis ac accumsan lacus. Integer luctus enim id felis sagittis, vel tempor mauris pulvinar. Maecenas ultricies lectus ligula, at porta nulla aliquet in. Integer scelerisque, magna sit amet mattis ornare, erat dolor ullamcorper velit, ut condimentum tellus ipsum ac elit. Suspendisse at eros interdum, bibendum dui vitae, porttitor mi. Mauris malesuada varius magna, ut porta nisi rutrum vitae. Aenean mattis dui ac ullamcorper rhoncus. Proin eu turpis tincidunt, sodales odio eu, auctor risus. Nam aliquet ultricies lacus. Praesent aliquet massa et sagittis sagittis. Sed a nulla in dui ultrices viverra sed ac eros. Nam tincidunt lectus in tempus eleifend. Donec et fermentum ante. Etiam lacinia tincidunt ante vel convallis.</p>
      <p>Pellentesque habitant morbi tristique senectus et netus et malesuada fames ac turpis egestas. Donec et eros hendrerit, aliquam velit dapibus, lobortis velit. Nam sed tempor ipsum. Fusce fermentum vitae turpis eget hendrerit. Donec egestas blandit aliquet. Aliquam at metus at felis bibendum porta non at nisl. Pellentesque habitant morbi tristique senectus et netus et malesuada fames ac turpis egestas. Praesent ultricies fringilla diam, a pretium turpis consectetur id. Cum sociis natoque penatibus et magnis dis parturient montes, nascetur ridiculus mus. Duis sed dolor urna. Phasellus quis tristique augue, sed molestie neque. Ut pulvinar orci ut tortor molestie interdum. Morbi a justo pulvinar leo venenatis rutrum nec sed neque. Aenean vitae imperdiet ipsum, vitae venenatis tellus. Nulla non elit et ligula sagittis vulputate.</p>
      <p>Praesent ac elit ligula. Sed sed arcu elit. Nam sit amet ligula in arcu consequat volutpat. Nunc lacinia tellus eros, tempor pulvinar nisi consequat sit amet. Aliquam aliquet eleifend blandit. Mauris sollicitudin lobortis arcu. Fusce consequat, lorem et dignissim adipiscing, risus urna dignissim tortor, quis bibendum turpis lorem at lorem.</p>
    </section>

    <div class="corner-art" role="img" aria-label="Large green geometric brand decoration in the lower left corner"></div>

    <footer class="partner">
      <span class="partner-shape"></span>
      <span class="partner-label">
        <span class="partner-member">member</span>
        <span class="partner-name">PLVAQT</span>
      </span>
    </footer>
  </main>
</body>
</html>
```